TR Ventura Website (professional site for investors and funds)

We want to make a website for an Holding Company that owns other companies' shares in different fields. TR is the name of the holding.
We still do not have a logo or preferred colors for the company. The company, through this website, will send a clear message: it's not important where we are, it's important what we do but more than that why we do what we do.
We search for inspiration in a simple layout because we want that the user feels comfortable and guided while exploring it. The content of the website aspire to be very impressive through one or more background images.

Below, the structure of the pages explained shortly.
To learn more, we have attached a draft of the website.

Home: page with a huge backround image that fill the whole page (maybe is better to merge the navbar with the image top color?).
About: with the same huge background image, we explain which are our fields.
Why: with the same huge background image, we explain which is our why.
Projects: dropdown list with project 1, project 2, project 3. If clicked, a box like about/why pops up in order to explain projects in detail.

Target Market(s)

Investors, Entrepreneurs

Industry/Entity Type

It Company

Number of Pages Required

4 page

Font styles to use
Sans Serif

Requirements
Must have
• An idea for the background image (color and design)
• Menu
• Page layout for about/why/projects
Nice to have
• Tips for color to use in this design
Should not have
• Complicated stuff

```html
<!DOCTYPE html>
<html lang="en">
<head>
<meta charset="utf-8">
<title>TR Ventura — About</title>
<link rel="stylesheet" href="https://fonts.googleapis.com/css2?family=Lato:wght@400;700;900&display=swap">
<style>
  :root {
    --ink: #ffffff;
    --rule: rgba(255, 255, 255, 0.45);
    --footer: #1b2c5a;
    --sky-top: #232b36;
    --sky-mid: #353a40;
    --city-low: #3b3429;
    --city-deep: #2a241c;
  }
  * { margin: 0; padding: 0; box-sizing: border-box; }
  html, body { width: 1200px; height: 845px; overflow: hidden; }
  body {
    position: relative;
    font-family: "Lato", sans-serif;
    color: var(--ink);
    background: var(--sky-top);
  }
  .hero-backdrop {
    position: absolute;
    inset: 0 0 61px 0;
    background:
      radial-gradient(ellipse at 50% 55%, rgba(90, 85, 70, 0.35), transparent 60%),
      linear-gradient(180deg, var(--sky-top) 0%, var(--sky-mid) 35%, var(--city-low) 70%, var(--city-deep) 100%);
  }
  .site-header { position: absolute; top: 0; left: 0; right: 0; height: 100px; }
  .brand {
    position: absolute; left: 125px; top: 32px;
    font-size: 36px; font-weight: 700; letter-spacing: 0.2px;
  }
  .main-nav { position: absolute; top: 36px; left: 0; right: 0; height: 43px; }
  .main-nav a {
    position: absolute; top: 0; height: 43px; line-height: 43px;
    color: var(--ink); text-decoration: none;
    font-size: 17.5px; font-weight: 700; text-align: center;
    transform: translateX(-50%);
  }
  .main-nav a.is-active {
    width: 100px; border: 2px solid var(--ink); line-height: 39px;
  }
  .content { position: absolute; left: 0; right: 0; top: 0; text-align: center; }
  .section-title {
    position: absolute; left: 0; right: 0;
    font-weight: 900; letter-spacing: -0.5px;
    text-shadow: 0 2px 6px rgba(0, 0, 0, 0.5);
  }
  .section-title--lead { font-size: 43px; top: 174px; }
  .section-title--sub { font-size: 27px; top: 401px; }
  .section-title--sub.consulting { top: 581px; }
  .section-text {
    position: absolute; left: 0; right: 0;
    font-size: 16px; line-height: 29px;
  }
  .divider {
    position: absolute; left: 204px; width: 802px; height: 1px; background: var(--rule);
  }
  .site-footer {
    position: absolute; left: 0; right: 0; bottom: 0; height: 61px;
    background: var(--footer);
  }
  .legal {
    position: absolute; left: 117px; top: 22px; font-size: 12.5px;
  }
  .legal span { margin-right: 6px; }
  .social { position: absolute; top: 21px; right: 0; left: 0; }
  .social a {
    position: absolute; transform: translateX(-50%);
    color: var(--ink); text-decoration: none; font-size: 12px; font-weight: 700;
  }
</style>
</head>
<body>
  <div class="hero-backdrop" role="img" aria-label="Dusk view over a dense city skyline with towers, darkened behind the text"></div>

  <header class="site-header">
    <div class="brand">TR Ventura</div>
    <nav class="main-nav">
      <a href="#" style="left:667px">Home</a>
      <a href="#" class="is-active" style="left:783px">About</a>
      <a href="#" style="left:903px">Why</a>
      <a href="#" style="left:1028px">Projects</a>
    </nav>
  </header>

  <main class="content">
    <h1 class="section-title section-title--lead">ABOUT US</h1>
    <p class="section-text" style="top:234px">
      Vivamus porttitor purus nisi eleifend libero a tempus libero lectus feugiat felis Morbi diam mauris<br>
      viverra in gravida eu mattis in ante Morbi eget arcu Morbi porta libero id ullamcorper nonummy nibh<br>
      ligula pulvinar metus eget consectetuer augue nisi quis lacus Ut ac mi quis lacus mollis aliquam<br>
      Curabitur iaculis tempus eros Curabitur vel mi sit amet magna malesuada
    </p>
    <div class="divider" style="top:372px"></div>

    <h2 class="section-title section-title--sub">OUR MISSION</h2>
    <p class="section-text" style="top:438px">
      Vivamus porttitor purus nisi eleifend libero a tempus libero lectus feugiat felis Morbi diam mauris<br>
      viverra in gravida eu mattis in ante Morbi eget arcu Morbi porta libero id ullamcorper nonummy nibh<br>
      ligula pulvinar metus eget consectetuer augue nisi quis lacus Ut ac mi quis
    </p>
    <div class="divider" style="top:554px"></div>

    <h2 class="section-title section-title--sub consulting">CONSULTING</h2>
    <p class="section-text" style="top:617px">
      Vivamus porttitor purus nisi eleifend libero a tempus libero lectus feugiat felis Morbi diam mauris<br>
      viverra in gravida eu mattis in ante Morbi eget arcu Morbi porta libero
    </p>
  </main>

  <footer class="site-footer">
    <p class="legal"><span>© 2017 Company Name</span><span>All right reserved</span><span>Term of Use</span></p>
    <nav class="social">
      <a href="#" style="left:926px">Relay</a>
      <a href="#" style="left:977px">Forum</a>
      <a href="#" style="left:1028px">Netlink</a>
      <a href="#" style="left:1076px">Circle</a>
    </nav>
  </footer>
</body>
</html>
```